Update of unique sports email website.

Hello.
I would like you to update a ol' archived website of mine. Bring it back to life with updated html5 or wordpress with plugins. I will provide the wordpress plugins by downloading from wordpress.org. It has 5-6 pages. Will need to update some stock sports photos.
It will be hosted on a vps server with linux and fantastico and softicious installed.
The website caters to the middle, junior, and high schools in america that has a mascot for their sports teams. The website will provide vanity email addresses that will be forwarded to their home/work/school email account. We will need a form that confirms valid email information on a form, send a confirmation page to the new clients email address that is given , they click that to confirm their enrollment. A paypal link to be installed.
I can and will provide the previous attempts of this website for any guidance and reflection to the new updated version. Other websites that are similar, or we like the design or copy : www.Brightpostal.net for frontpage colors and whitespace.
Target Market(s)
this updated website will have clicks from all over the world. the paying customer will be from mostly the united states. Sports audience. Middle schoolers, high schoolers, parents, coaches, teachers, students, administrators who all want a highly desirable sports email address of their favorite team, or local high school .
Talvix Marketing has identified and acquired the most popular sports mascots in America's most popular high school sports. We want to offer these two-worded domains to the sports amateur market. No professional teams. Strictly high schools and young adults.
Industry/Entity Type
School
Requirements
Must have
- easy to read, easy to look at, easy on the eyes. Lots of white space. A few colors . Standard black text/fonts.
A paypal.com link to accept immediate payments. Then a confirmation email sent to him and us(talvix, inc) indicating the quick payment and start processing his email request by hand. A human will always look/check/verify the email address request.
Professional look. Classy look. Fast loading.
html5 complied.
Somekind of interesting header.
Need to handle the sports: Baseball, basketball, lacrosse(lax), football, volleyball, softball, track, and soccer.
Should not have
- sloppy text and pages.
ugly colors and combinations.
Lots of questions.

```html
<!DOCTYPE html>
<html lang="en">
<head>
<meta charset="utf-8">
<title>TeamPostBox.com</title>
<link href="https://fonts.googleapis.com/css2?family=Anton&family=Arimo:wght@400;700&family=Ubuntu:wght@400;500&display=swap" rel="stylesheet">
<style>
:root{
  --red:#ff0000;
  --brand-red:#e8141b;
  --white:#ffffff;
  --text-grey:#7a7a7a;
  --label:#8a1a2a;
  --field:#fdfaf0;
  --field-line:#efe3c4;
  --box-line:#dcdcdc;
  --footer:#161616;
  --orange:#f7941d;
  --link-orange:#e8861a;
}
*{box-sizing:border-box;margin:0;padding:0}
html,body{width:1200px;height:799px;overflow:hidden;background:var(--white)}
body{position:relative;font-family:"Arimo",Arial,sans-serif}
.abs{position:absolute}

.brand{left:160px;top:22px;font-family:"Anton",sans-serif;font-size:32px;line-height:42px;color:var(--brand-red);letter-spacing:.5px}

.main-nav{left:0;top:89px;width:1200px;height:42px;background:var(--red)}
.main-nav ul{list-style:none;position:absolute;left:229px;top:0;display:flex;height:42px}
.main-nav li{font-family:"Anton",sans-serif;font-size:15px;color:var(--white);line-height:40px;text-transform:uppercase;padding:0 22px;position:relative}
.main-nav li.active::after{content:"";position:absolute;left:0;right:0;bottom:3px;height:2px;background:var(--white)}

.hero{left:157px;top:136px;width:604px;height:181px;background:radial-gradient(ellipse at 40% 55%,#d9d4c8 0%,#b8503a 38%,#2a1a14 75%,#0a0a0a 100%)}

.login{left:770px;top:141px;width:266px;height:226px;border:1px solid var(--box-line);padding:12px 15px 0 15px}
.login h2{font-family:"Arimo",sans-serif;font-weight:700;font-size:13px;color:var(--red);margin-bottom:20px}
.login label{display:block;font-size:12px;color:var(--label);margin-left:5px;margin-bottom:2px}
.login .field{width:135px;height:30px;margin-left:5px;background:var(--field);border:1px solid var(--field-line);margin-bottom:10px}
.login .remember{display:flex;align-items:center;gap:6px;margin-left:5px;font-size:12px;color:var(--label);margin-top:-2px}
.login .check{width:10px;height:10px;border:1px solid #888;background:#fff;display:flex;align-items:center;justify-content:center}
.btn{display:inline-flex;align-items:center;justify-content:center;background:linear-gradient(#fafafa,#e2e2e2);border:1px solid #cfcfcf;border-radius:3px;color:var(--red);font-size:13px;box-shadow:0 1px 2px rgba(0,0,0,.15)}
.login .btn{width:72px;height:27px;margin:12px 0 0 5px}
.login .lost{margin-top:8px;font-size:11px;color:#666;text-decoration:underline;display:flex;align-items:center;gap:6px}
.login .lost span.arrow{text-decoration:none;font-size:11px;color:#555}

.welcome{left:161px;top:364px;font-family:"Anton",sans-serif;font-size:21px;color:var(--red);text-transform:uppercase}
.intro{left:161px;top:401px;width:600px;font-size:13px;line-height:19.5px;color:var(--text-grey)}
.mascots-btn{left:662px;top:467px;width:87px;height:27px}

.thumb{top:519px;height:46px}
.thumb-hockey{left:161px;width:279px;background:linear-gradient(90deg,#e6e6e6,#9a9a9a 60%,#d0d0d0)}
.thumb-football{left:478px;width:278px;background:linear-gradient(90deg,#3a2c2a,#7b3b34 45%,#c9c9c9)}

.site-footer{left:0;top:581px;width:1200px;height:218px;background:var(--footer)}
.foot-col{top:54px;font-family:"Ubuntu",sans-serif}
.foot-col h3{font-size:14px;font-weight:500;color:var(--orange);margin-bottom:14px}
.foot-col ul{list-style:none}
.foot-col li{font-size:12px;line-height:14.5px;color:var(--link-orange)}
.col-info{left:188px}
.col-contact{left:352px}
.col-company{left:530px}
.foot-brand{left:758px;top:50px;font-family:"Anton",sans-serif;font-size:21px;line-height:28px;color:var(--brand-red)}
.social{left:757px;top:89px;display:flex;gap:9px}
.social span{width:28px;height:28px;border-radius:50%;display:block}
.social .s1{background:var(--orange)}
.social .s2{background:#3b6bb0}
.social .s3{background:#2bb3d6}
.copyright{left:0;top:174px;width:1200px;text-align:center;font-size:12px;color:var(--white)}
</style>
</head>
<body>
<header>
  <div class="abs brand">TEAMPOSTBOX.COM</div>
  <nav class="abs main-nav">
    <ul>
      <li class="active">Home</li>
      <li>Mascots</li>
      <li>About Us</li>
      <li>Merchandise</li>
      <li>F.A.Q.</li>
      <li>Investors</li>
      <li>Contact Us</li>
    </ul>
  </nav>
</header>

<main>
  <div class="abs hero" role="img" aria-label="Pile of sports balls: basketball, soccer balls, volleyball, football, tennis ball, hockey puck, boxing gloves and baseball glove"></div>

  <form class="abs login">
    <h2>Log In</h2>
    <label>Username</label>
    <div class="field"></div>
    <label>Password</label>
    <div class="field"></div>
    <div class="remember">Remember Me
      <span class="check"><svg width="8" height="8" viewBox="0 0 8 8"><path d="M1 4 L3 6.5 L7 1" fill="none" stroke="#333" stroke-width="1.5"/></svg></span>
    </div>
    <div class="btn">Log In</div>
    <div class="lost"><span class="arrow">›</span>Lost your password?</div>
  </form>

  <h1 class="abs welcome">Welcome to TeamPostBox.com</h1>
  <p class="abs intro">The Internet’s Largest Purveyor of High Schools, Colleges, and Universities Nicknames and Team Mascots for Email and Team Websites. View our Serious collection of America’s Most Famous Nicknames and Team Mascots. Each Will Be Available For All Your Team Email Needs.</p>
  <div class="abs btn mascots-btn">Mascots</div>

  <div class="abs thumb thumb-hockey" role="img" aria-label="Hockey players in action"></div>
  <div class="abs thumb thumb-football" role="img" aria-label="Football players in action"></div>
</main>

<footer class="abs site-footer">
  <div class="abs foot-col col-info">
    <h3>Information</h3>
    <ul><li>Organization</li><li>Schedule</li><li>Pessoas</li><li>Management</li></ul>
  </div>
  <div class="abs foot-col col-contact">
    <h3>Contact</h3>
    <ul><li>Area Map</li><li>Address</li><li>Contact Us</li></ul>
  </div>
  <div class="abs foot-col col-company">
    <h3>Company</h3>
    <ul><li>About Us</li><li>Terms</li></ul>
  </div>
  <div class="abs foot-brand">TEAMPOSTBOX.COM</div>
  <div class="abs social" aria-label="Social links"><span class="s1"></span><span class="s2"></span><span class="s3"></span></div>
  <p class="abs copyright">© Copyright 2014 TeamPostBox.com. All Rights Reserved.</p>
</footer>
</body>
</html>
```